Business Card Design for Occupational Medicine Start Up Company

We need to design a professional business card. We are a healthcare company providing occupational medicine services to blue collar industries. We are professional, efficient and high quality service providers.

Target Market(s)

Blue Collar Industry: Shipbuilding, Ports, Trucking Companies; The Executives and Safety Officers for these companies

Industry/Entity Type

Healthcare

Contact Information for Business Card

Logo, Name, Title, Email, Phone

Other font styles liked:
• Please match our Brand Guide

Requirements
Must have
• Our Company Colors and Logo

```html
<!DOCTYPE html>
<html lang="en">
<head>
<meta charset="utf-8">
<title>CrewWell Clinics – Business Card</title>
<link href="https://fonts.googleapis.com/css2?family=Montserrat:wght@400;500;600;700&family=Roboto:wght@400&display=swap" rel="stylesheet">
<style>
  :root {
    --backdrop: #2a2a2a;
    --navy: #2f2f8a;
    --navy-ink: #2b2e7c;
    --sky: #2aa0da;
    --amber: #f2a93b;
    --paper: #f4f4f2;
    --white: #ffffff;
  }
  * { margin: 0; padding: 0; box-sizing: border-box; }
  html, body {
    width: 1200px; height: 1200px; overflow: hidden;
    background: var(--backdrop);
  }
  .canvas { position: relative; width: 1200px; height: 1200px; }

  .card {
    position: absolute;
    width: 593px; height: 349px;
    border-radius: 24px;
    overflow: hidden;
  }
  .card--front { left: 299px; top: 199px; background: var(--navy); }
  .card--back  { left: 293px; top: 638px; background: var(--paper); }

  /* portrait content area turned to read bottom-to-top */
  .card__body {
    position: absolute;
    left: 50%; top: 50%;
    width: 349px; height: 593px;
    transform: translate(-50%, -50%) rotate(-90deg);
  }

  /* front */
  .front__brand {
    position: absolute; left: 0; right: 0; top: 190px;
    display: flex; flex-direction: column; align-items: center; gap: 22px;
  }
  .brand-dot {
    width: 70px; height: 70px; border-radius: 50%;
    background: var(--amber);
  }
  .brand-name {
    font-family: "Montserrat", sans-serif;
    font-weight: 600; font-size: 27px; letter-spacing: 1px;
    text-transform: uppercase; white-space: nowrap;
  }
  .front__brand .brand-name { color: var(--white); }
  .front__web {
    position: absolute; left: 0; right: 0; top: 540px;
    text-align: center;
    font-family: "Montserrat", sans-serif; font-size: 15px; letter-spacing: 0.5px;
    color: var(--white);
  }
  .front__web .hl-sky { color: var(--sky); }
  .front__web .hl-amber { color: var(--amber); }

  /* back */
  .back__brand {
    position: absolute; left: 0; right: 0; top: 62px;
    display: flex; flex-direction: column; align-items: center; gap: 22px;
  }
  .back__brand .brand-dot { width: 64px; height: 64px; }
  .back__brand .brand-name { color: var(--navy-ink); }

  .person { position: absolute; left: 0; right: 0; top: 292px; text-align: center; }
  .person__name {
    font-family: "Montserrat", sans-serif; font-weight: 500;
    font-size: 24px; letter-spacing: 0.5px; color: var(--sky);
    text-transform: uppercase;
  }
  .person__title {
    font-family: "Roboto", sans-serif; font-size: 14px; color: var(--navy-ink);
    margin-top: 2px;
  }

  .divider {
    position: absolute; left: 0; right: 0; top: 378px;
    display: flex; align-items: center; justify-content: center; gap: 10px;
  }
  .divider__line { width: 74px; height: 2px; background: var(--sky); }
  .divider__icons { display: flex; gap: 4px; }

  .contact {
    position: absolute; left: 0; right: 0; top: 412px;
    text-align: center;
    font-family: "Roboto", sans-serif; font-size: 15px; line-height: 23px;
    color: var(--navy-ink);
  }
  .contact__address { margin-top: 12px; }
</style>
</head>
<body>
<div class="canvas">

  <section class="card card--front">
    <div class="card__body">
      <div class="front__brand">
        <span class="brand-dot"></span>
        <span class="brand-name">CrewWell Clinics</span>
      </div>
      <p class="front__web">www.<span class="hl-sky">crewwell</span><span class="hl-amber">clinics</span>.com</p>
    </div>
  </section>

  <section class="card card--back">
    <div class="card__body">
      <div class="back__brand">
        <span class="brand-dot"></span>
        <span class="brand-name">CrewWell Clinics</span>
      </div>

      <div class="person">
        <p class="person__name">Dana Hale</p>
        <p class="person__title">Senior Doctor</p>
      </div>

      <div class="divider">
        <span class="divider__line"></span>
        <div class="divider__icons">
          <svg class="icon icon--phone" width="16" height="16" viewBox="0 0 16 16" aria-label="Phone">
            <circle cx="8" cy="8" r="7.5" fill="none" stroke="#f2a93b"/>
            <circle cx="8" cy="8" r="5.5" fill="#f2a93b"/>
            <path d="M5.6 5.2c.4-.4.8-.3 1 .1l.5.9c.1.3 0 .5-.2.7l-.3.3c.3.7.9 1.3 1.6 1.6l.3-.3c.2-.2.4-.3.7-.2l.9.5c.4.2.5.6.1 1-.6.6-1.4.7-2.2.2-1.2-.7-2.2-1.7-2.8-2.9-.4-.7-.2-1.4.4-1.9z" fill="#fff"/>
          </svg>
          <svg class="icon icon--mail" width="16" height="16" viewBox="0 0 16 16" aria-label="Email">
            <circle cx="8" cy="8" r="7.5" fill="none" stroke="#f2a93b"/>
            <circle cx="8" cy="8" r="5.5" fill="#f2a93b"/>
            <rect x="5" y="6" width="6" height="4.2" fill="none" stroke="#fff" stroke-width="0.9"/>
            <path d="M5 6l3 2.3L11 6" fill="none" stroke="#fff" stroke-width="0.9"/>
          </svg>
          <svg class="icon icon--web" width="16" height="16" viewBox="0 0 16 16" aria-label="Website">
            <circle cx="8" cy="8" r="7.5" fill="none" stroke="#f2a93b"/>
            <circle cx="8" cy="8" r="5.5" fill="#f2a93b"/>
            <circle cx="8" cy="8" r="3" fill="none" stroke="#fff" stroke-width="0.8"/>
            <path d="M5 8h6M8 5c-1.3 1.8-1.3 4.2 0 6M8 5c1.3 1.8 1.3 4.2 0 6" fill="none" stroke="#fff" stroke-width="0.8"/>
          </svg>
        </div>
        <span class="divider__line"></span>
      </div>

      <div class="contact">
        <p class="contact__phone">555-210-4830</p>
        <p class="contact__email">hello@crewwell.com</p>
        <p class="contact__web">www.crewwell.com</p>
        <div class="contact__address">
          <p>48 Harbor Road, Suite 210</p>
          <p>Bay Point, State 20415</p>
        </div>
      </div>
    </div>
  </section>

</div>
</body>
</html>
```